Hero Image Redesign for VELM Consulting Website

About us:
VELM Consulting is an organisational psychology and human resource management consulting firm based in Melbourne, Australia (www.velmadvisory-example.com.au). We are a B2B offering a range of organisational psychology measurement and consulting. The largest part of our business is our online psychometric assessments, which are self-managed via an online portal, which is currently used by many organisations worldwide as part of their recruitment process.

What we are looking for:
We are seeking assistance to redesign an image located above the fold - on the top right hand side of homepage. We want an image of a small group of diverse people happily working together using a laptop (either individually or as a group), overlayed with graphic representations reflective of using our online Psychometric Assessment tool, in an interactive fashion.

The graphics will highlight key features of the self-service VELM Psychometric Assessment Portal, specifically ease of use, flexibility and our integrated approach. We want the image to look clean, clear, minimal, with use of negative space. All graphics must be accessible (including sufficient colour contrast and text size).

We would like the graphic to feature 3 “pop ups” highlighting features, and these should appear over the image:

1. Setup participants easily online
2. Check the status of an assessment
3. View participants’ reports

Examples from other SaaS websites attached.

The final design should communicate trust, reliability, our scientific evidence based approach, and our approachable and friendly customer service.

Our main brand colours are:
• Navy – HEX #2F2971
• Mid Blue – HEX #0C75C0
• Black – HEX #000000

About VELM’ website and potential for future work:

• VELM’ website pages have been created using Bricks Builder for WordPress.
• There is a strong possibility of future projects following successful delivery. We are an excellent client – ethical, professional and with a genuine commitment to partnership.

Need extra days to review

```html
<!DOCTYPE html>
<html lang="en">
<head>
<meta charset="utf-8">
<title>VELM Consulting – Organisational Psychology Consulting</title>
<link rel="stylesheet" href="https://fonts.googleapis.com/css2?family=Plus+Jakarta+Sans:wght@400;500;600;700&display=swap">
<style>
  :root {
    --navy: #2f2971;
    --aqua: #9fe6dd;
    --aqua-soft: #a8e3dc;
    --link: #8fe3d8;
    --nav-bg: #f5f5f5;
    --text: #222;
    --muted: #4a4a4a;
    --white: #fff;
  }
  * { box-sizing: border-box; margin: 0; padding: 0; }
  html, body { width: 1200px; height: 675px; overflow: hidden; background: var(--white); }
  body { font-family: "Plus Jakarta Sans", sans-serif; color: var(--text); position: relative; }

  .announcement {
    height: 40px; background: var(--navy); color: var(--white);
    display: flex; align-items: center; justify-content: center;
    font-size: 13px; font-weight: 500; gap: 6px;
  }
  .announcement a { color: var(--link); text-decoration: underline; }

  .site-header {
    height: 64px; background: var(--nav-bg);
    display: flex; align-items: center; justify-content: space-between;
    padding: 0 51px 0 37px;
  }
  .brand { display: flex; align-items: center; gap: 8px; font-size: 22px; font-weight: 700; color: var(--navy); }
  .brand-mark { width: 18px; height: 18px; border-radius: 50%; background: var(--aqua); }
  .main-nav { display: flex; gap: 27px; font-size: 13.5px; color: var(--text); }
  .main-nav span { display: flex; align-items: center; gap: 6px; }
  .main-nav svg { width: 10px; height: 10px; }

  .hero-copy { position: absolute; left: 67px; top: 167px; width: 530px; }
  .hero-title { font-size: 60px; line-height: 67px; font-weight: 600; color: var(--navy); letter-spacing: -0.3px; }
  .hero-lead { margin-top: 34px; font-size: 21px; line-height: 38px; color: var(--muted); }
  .hero-actions { margin-top: 22px; display: flex; gap: 35px; }
  .btn { height: 52px; display: flex; align-items: center; justify-content: center; gap: 8px;
    font-size: 15.5px; font-weight: 600; border-radius: 3px; box-shadow: 0 3px 6px rgba(0,0,0,.15); }
  .btn-primary { width: 198px; background: var(--navy); color: var(--white); }
  .btn-secondary { width: 199px; background: var(--aqua-soft); color: var(--navy); }

  .hero-visual { position: absolute; left: 625px; top: 160px; width: 530px; height: 420px; }
  .hero-photo { position: absolute; left: 71px; top: 45px; width: 396px; height: 311px;
    background: linear-gradient(135deg, #e9e9e7 0%, #d6d4d0 45%, #b99a74 80%, #8f6e4c 100%); }
  .popup { position: absolute; background: var(--aqua); border-radius: 10px;
    display: flex; align-items: center; gap: 8px; padding: 0 12px;
    font-size: 9.5px; font-weight: 600; color: #111; }
  .popup svg.icon { width: 30px; height: 30px; flex: none; }
  .popup .tail { position: absolute; width: 20px; height: 20px; }
  .popup-setup { left: 309px; top: 9px; width: 209px; height: 58px; }
  .popup-setup .tail { left: 20px; bottom: -16px; }
  .popup-status { left: 6px; top: 352px; width: 218px; height: 57px; }
  .popup-status .tail { right: 20px; top: -16px; }
  .popup-reports { left: 323px; top: 352px; width: 174px; height: 57px; }
  .popup-reports .tail { left: 18px; top: -16px; }
</style>
</head>
<body>
  <div class="announcement">
    Register now for our <a href="#">free virtual workshops</a> | VELM Consulting Clients: <a href="#">Login to the Portal</a>
  </div>

  <header class="site-header">
    <div class="brand"><span class="brand-mark"></span>VELM Consulting</div>
    <nav class="main-nav">
      <span>Psychometric testing <svg viewBox="0 0 10 10"><path d="M1 3l4 4 4-4" fill="none" stroke="#222" stroke-width="1.5"/></svg></span>
      <span>Employee wellbeing <svg viewBox="0 0 10 10"><path d="M1 3l4 4 4-4" fill="none" stroke="#222" stroke-width="1.5"/></svg></span>
      <span>HR consulting <svg viewBox="0 0 10 10"><path d="M1 3l4 4 4-4" fill="none" stroke="#222" stroke-width="1.5"/></svg></span>
      <span>Events</span>
      <span>Knowledge hub <svg viewBox="0 0 10 10"><path d="M1 3l4 4 4-4" fill="none" stroke="#222" stroke-width="1.5"/></svg></span>
      <span>About us <svg viewBox="0 0 10 10"><path d="M1 3l4 4 4-4" fill="none" stroke="#222" stroke-width="1.5"/></svg></span>
      <span>Contact</span>
    </nav>
  </header>

  <section class="hero-copy">
    <h1 class="hero-title">Organisational Psychology Consulting</h1>
    <p class="hero-lead">Optimise your workforce with psychometric testing, engagement surveys, wellbeing measures, and organisational development.</p>
    <div class="hero-actions">
      <a class="btn btn-primary">Psychometric Testing</a>
      <a class="btn btn-secondary">Speak to an Expert <span>→</span></a>
    </div>
  </section>

  <div class="hero-visual">
    <div class="hero-photo" role="img" aria-label="Photo of a smiling professional working on a laptop at a desk in a bright office"></div>

    <div class="popup popup-setup">
      <svg class="icon" viewBox="0 0 30 30" fill="none" stroke="#2f2971" stroke-width="1.5">
        <circle cx="15" cy="10" r="3.5"/><circle cx="7" cy="14" r="3"/><circle cx="23" cy="14" r="3"/>
        <path d="M9 24c0-4 3-7 6-7s6 3 6 7z"/><path d="M2 24c0-3 2-5 5-5M28 24c0-3-2-5-5-5"/>
      </svg>
      Setup participants easily online
      <svg class="tail" viewBox="0 0 20 20"><path d="M0 0h16L2 20z" fill="#9fe6dd"/></svg>
    </div>

    <div class="popup popup-status">
      <svg class="icon" viewBox="0 0 30 30" fill="none" stroke="#2f2971" stroke-width="1.5">
        <rect x="4" y="4" width="17" height="23" rx="1"/><path d="M8 10h2M8 15h2M8 20h2M12 10h5"/>
        <circle cx="20" cy="19" r="4.5"/><path d="M23 22l5 5"/>
      </svg>
      Check the status of an assessment
      <svg class="tail" viewBox="0 0 20 20"><path d="M20 0v20H0z" fill="#9fe6dd"/></svg>
    </div>

    <div class="popup popup-reports">
      <svg class="icon" viewBox="0 0 30 30" fill="none" stroke="#2f2971" stroke-width="1.5">
        <rect x="9" y="3" width="13" height="15" rx="1"/><path d="M12 8h7M12 12h7"/>
        <circle cx="8" cy="21" r="2.5"/><circle cx="22" cy="21" r="2.5"/><path d="M3 28c0-3 2-4 5-4s5 1 5 4M17 28c0-3 2-4 5-4s5 1 5 4"/>
      </svg>
      View participants’ reports
      <svg class="tail" viewBox="0 0 20 20"><path d="M0 0l18 20H0z" fill="#9fe6dd"/></svg>
    </div>
  </div>
</body>
</html>
```